New Zealand Luggage Importer Needs Business Cards

We need professional, creative and fashionable business cards created.
We are based in New Zealand and import and distribute high-end, quality, fashionable and durable luggage.
We pride ourselves on selling the very best quality luggage, second only to 1 brand (which we won't mention here)...we use the same manufacturer. However, our prices are much more reasonable.
Industry/Entity Type
Business
Contact Information for Business Card
Mark Dunsley
027 512 4068
3/17 Harlow Street, Pinecrest Flats, Auckland, 0614
PO Box 204377, Fernside, Auckland 0731
09-528-3916
sales@brivancases.co.nz / www.brivancases.co.nz

```html
<!DOCTYPE html>
<html lang="en">
<head>
<meta charset="utf-8">
<title>Brivan Cases – Business Card</title>
<link href="https://fonts.googleapis.com/css2?family=Montserrat:wght@300;400;500;600;700&display=swap" rel="stylesheet">
<style>
  :root {
    --page-bg: #dfe4ea;
    --card-black: #1c1c1f;
    --rule-white: #e9e9ec;
    --text-white: #f4f4f6;
    --gold-light: #f6dc86;
    --gold-dark: #b78a2a;
    --band-light: #c9ccd3;
    --band-mid: #a9aebb;
    --band-text: #1e1f24;
    --pin-dark: #26272c;
  }
  * { box-sizing: border-box; margin: 0; padding: 0; }
  html, body {
    width: 1200px; height: 900px; overflow: hidden;
    background: var(--page-bg);
    font-family: "Montserrat", sans-serif;
  }
  .card {
    position: absolute; left: 100px; top: 165px;
    width: 1000px; height: 570px;
    background: var(--card-black);
    box-shadow: 0 14px 40px rgba(0,0,0,0.25);
    overflow: hidden;
  }
  .brand {
    position: absolute; top: 98px; left: 0; width: 100%;
    text-align: center;
    font-weight: 600; font-size: 52px; letter-spacing: 2px;
    color: var(--rule-white);
  }
  .name-row {
    position: absolute; top: 212px; left: 0; width: 100%;
    display: flex; align-items: center; gap: 22px;
  }
  .name-row .rule { flex: 1; height: 3px; background: var(--rule-white); }
  .person {
    font-size: 40px; color: var(--text-white); letter-spacing: 1px;
    font-weight: 400; white-space: nowrap;
  }
  .person strong { font-weight: 700; }
  .contact {
    position: absolute; display: flex; align-items: center; gap: 16px;
    font-size: 25px; color: var(--text-white); font-weight: 400;
  }
  .icon-gold {
    width: 32px; height: 32px; border-radius: 50%;
    background: linear-gradient(160deg, var(--gold-light), var(--gold-dark));
    display: flex; align-items: center; justify-content: center;
  }
  .address-band {
    position: absolute; top: 429px; left: 0; width: 100%; height: 91px;
    background: linear-gradient(90deg, var(--band-mid), var(--band-light) 45%, var(--band-mid));
  }
  .address {
    position: absolute; top: 20px; display: flex; gap: 14px;
    font-size: 21px; line-height: 27px; color: var(--band-text);
  }
  .icon-pin {
    width: 30px; height: 30px; border-radius: 50%; background: var(--pin-dark);
    display: flex; align-items: center; justify-content: center; flex-shrink: 0;
  }
</style>
</head>
<body>
  <section class="card">
    <div class="brand">BRIVAN CASES</div>

    <div class="name-row">
      <span class="rule"></span>
      <span class="person">MARK <strong>DUNSLEY</strong></span>
      <span class="rule"></span>
    </div>

    <div class="contact" style="left:70px; top:300px;">
      <span class="icon-gold"><svg width="18" height="18" viewBox="0 0 24 24"><path fill="#2a2a2a" d="M6.6 10.8a15 15 0 0 0 6.6 6.6l2.2-2.2a1 1 0 0 1 1-.25 11.4 11.4 0 0 0 3.6.6 1 1 0 0 1 1 1V20a1 1 0 0 1-1 1A17 17 0 0 1 3 4a1 1 0 0 1 1-1h3.5a1 1 0 0 1 1 1c0 1.25.2 2.45.6 3.6a1 1 0 0 1-.25 1z"/></svg></span>
      <span>09-528-3916</span>
    </div>
    <div class="contact" style="left:70px; top:350px;">
      <span class="icon-gold"><svg width="18" height="18" viewBox="0 0 24 24"><path fill="#2a2a2a" d="M6.6 10.8a15 15 0 0 0 6.6 6.6l2.2-2.2a1 1 0 0 1 1-.25 11.4 11.4 0 0 0 3.6.6 1 1 0 0 1 1 1V20a1 1 0 0 1-1 1A17 17 0 0 1 3 4a1 1 0 0 1 1-1h3.5a1 1 0 0 1 1 1c0 1.25.2 2.45.6 3.6a1 1 0 0 1-.25 1z"/></svg></span>
      <span>027 512 4068</span>
    </div>
    <div class="contact" style="left:554px; top:300px;">
      <span class="icon-gold"><svg width="20" height="20" viewBox="0 0 24 24" fill="none" stroke="#2a2a2a" stroke-width="2"><circle cx="12" cy="12" r="9"/><path d="M3 12h18M12 3c3 3 3 15 0 18M12 3c-3 3-3 15 0 18"/></svg></span>
      <span>www.brivancases.co.nz</span>
    </div>
    <div class="contact" style="left:554px; top:350px;">
      <span class="icon-gold"><svg width="18" height="18" viewBox="0 0 24 24"><rect x="3" y="6" width="18" height="12" fill="#2a2a2a"/><path d="M3 6l9 7 9-7" fill="none" stroke="#d9b860" stroke-width="1.5"/></svg></span>
      <span>sales@brivancases.co.nz</span>
    </div>

    <div class="address-band">
      <div class="address" style="left:70px;">
        <span class="icon-pin"><svg width="14" height="16" viewBox="0 0 24 28"><path fill="#e0e0e0" d="M12 0a9 9 0 0 0-9 9c0 7 9 19 9 19s9-12 9-19a9 9 0 0 0-9-9zm0 12.5A3.5 3.5 0 1 1 12 5.5a3.5 3.5 0 0 1 0 7z"/></svg></span>
        <span>3/17 Harlow Street, Pinecrest Flats<br>Auckland 0614</span>
      </div>
      <div class="address" style="left:554px;">
        <span class="icon-pin"><svg width="14" height="16" viewBox="0 0 24 28"><path fill="#e0e0e0" d="M12 0a9 9 0 0 0-9 9c0 7 9 19 9 19s9-12 9-19a9 9 0 0 0-9-9zm0 12.5A3.5 3.5 0 1 1 12 5.5a3.5 3.5 0 0 1 0 7z"/></svg></span>
        <span>PO Box 204377, Fernside<br>Auckland 0731</span>
      </div>
    </div>
  </section>
</body>
</html>
```